Renowned Chiropractic Clinic needs unique and professional business card

We need a clean and professional looking business card that embodies our core values and stands for excellence. Highest standard of care and trustworthiness is what we want a future patient to connect to the design of the business card.
Ideally we want the design of the business card to be unique in nature and have a close connection to the SPINE as it is the core of what we do in our office - working with peoples spines.

Contact Information for Business Card

Font file is modified Nexa light and Montserrat medium. Colors are #5BC9E1, #666666, and #9dd5eb

On the front we would like to have the logo and the name of the office with an engaging, trustworthy and professional design.
On the back we need an area for our address, phone number and email address (This can be also be in the front).
On the back we would also like the slogan (this is however not a must and can also be on the front).

The HEXAGON (the design from the spine), could be an idea for the design to evolve around - this is however up to your professional creativity!

Requirements
Must have
• I want the design to primarily evolve around the HEXAGON shape and to have as few curves in it as possible. Therefore, making the design as "edgy" and "linear" as possible.

- Logo
- German Address Line (we are moving offices so we do not yet have a physical address so it would have to be a placeholder address for now that can be changed) --> Office Name (Line 1), Streetname (Line 2), Zip Code and Town (Line 3)
- email and phone number field
Nice to have
• Incorporation of the slogan "Kehren Sie Ihren Problemen den Rücken"

Please let your imagination run free :)!!! I am excited to work with you all to create an astonishing business card!

```html
<!DOCTYPE html>
<html lang="de">
<head>
<meta charset="utf-8">
<title>Chiropraxis Verta – Visitenkarte</title>
<link href="https://fonts.googleapis.com/css2?family=Montserrat:wght@500;700&family=Questrial&display=swap" rel="stylesheet">
<style>
  :root{
    --teal:#5bc9e1;
    --teal-soft:#9dd5eb;
    --petrol:#1f7196;
    --petrol-deep:#106b90;
    --steel:#5f98a8;
    --grey:#666666;
    --ink:#555555;
    --white:#ffffff;
    --page:#ffffff;
  }
  html,body{margin:0;padding:0;overflow:hidden;}
  body{width:1200px;height:1200px;background:var(--page);position:relative;}
  .card{position:absolute;left:198px;width:814px;height:493px;overflow:hidden;}
  .card-front{top:79px;background:var(--white);}
  .card-back{top:628px;background:var(--grey);}
  .card-art{position:absolute;inset:0;width:100%;height:100%;}

  .brand-mark{position:absolute;left:291px;top:71px;width:162px;height:162px;box-sizing:border-box;border:2px solid var(--teal);border-radius:50%;}

  .brand{position:absolute;font-family:"Questrial",sans-serif;font-weight:400;margin:0;}
  .brand-front{left:457px;top:177px;color:var(--teal);}
  .brand-back{left:69px;top:360px;color:var(--white);}
  .brand-kicker{display:block;font-size:15px;letter-spacing:13px;line-height:1;margin-left:2px;}
  .brand-name{display:block;font-size:68px;letter-spacing:3px;line-height:1;margin-top:4px;}
  .brand-back .brand-kicker{font-size:12px;letter-spacing:11px;margin-left:16px;}
  .brand-back .brand-name{font-size:54px;margin-top:4px;}

  .slogan{position:absolute;left:301px;top:276px;margin:0;font-family:"Montserrat",sans-serif;font-weight:500;font-size:20px;color:var(--ink);white-space:nowrap;}

  .holder{position:absolute;left:430px;top:106px;margin:0;}
  .holder-name{display:block;font-family:"Montserrat",sans-serif;font-weight:700;font-size:36px;letter-spacing:2px;color:var(--white);line-height:1.05;}
  .holder-role{display:block;font-family:"Questrial",sans-serif;font-size:31px;color:#e6e6e6;letter-spacing:.8px;line-height:1.25;}

  .contact-list{position:absolute;left:430px;top:310px;margin:0;padding:0;list-style:none;font-family:"Montserrat",sans-serif;font-weight:500;font-size:16px;color:var(--white);line-height:1;}
  .contact-item{display:flex;align-items:center;gap:12px;margin-bottom:14px;}
  .contact-phone{letter-spacing:1.6px;}
  .contact-icon{flex:none;width:28px;height:28px;}
</style>
</head>
<body>

<section class="card card-front" aria-label="Vorderseite">
  <svg class="card-art" viewBox="0 0 1302 788" preserveAspectRatio="none" aria-hidden="true">
    <defs>
      <linearGradient id="facet-down" x1="0" y1="0" x2="0" y2="1">
        <stop offset="0" stop-color="var(--steel)" stop-opacity=".08"/>
        <stop offset="1" stop-color="var(--steel)" stop-opacity=".95"/>
      </linearGradient>
      <linearGradient id="facet-side" x1="1" y1="0" x2="0" y2="0">
        <stop offset="0" stop-color="var(--steel)" stop-opacity=".05"/>
        <stop offset="1" stop-color="var(--steel)" stop-opacity=".9"/>
      </linearGradient>
      <linearGradient id="facet-up" x1="0" y1="1" x2="0" y2="0">
        <stop offset="0" stop-color="var(--steel)" stop-opacity=".08"/>
        <stop offset="1" stop-color="var(--steel)" stop-opacity=".95"/>
      </linearGradient>
      <linearGradient id="facet-teal" x1="0" y1="0" x2="1" y2="1">
        <stop offset="0" stop-color="var(--teal)"/>
        <stop offset="1" stop-color="var(--teal-soft)" stop-opacity=".6"/>
      </linearGradient>
    </defs>
    <polygon points="0,0 55,0 190,180 440,290 0,170" fill="url(#facet-down)"/>
    <polygon points="0,220 300,245 430,180 160,330 0,365" fill="url(#facet-side)"/>
    <polygon points="1302,788 1150,788 1000,660 820,582 1150,630 1302,705" fill="url(#facet-up)"/>
    <polygon points="1302,540 1150,545 820,685 1100,625 1302,660" fill="url(#facet-up)"/>
    <polygon points="0,610 90,610 190,700 190,788 0,788" fill="url(#facet-teal)" opacity=".75"/>
    <polygon points="0,740 90,685 200,685 280,788 0,788" fill="url(#facet-teal)" opacity=".7"/>
  </svg>

  <span class="brand-mark" aria-hidden="true"></span>
  <h1 class="brand brand-front">
    <span class="brand-kicker">CHIROPRAXIS</span>
    <span class="brand-name">VERTA</span>
  </h1>
  <p class="slogan">Kehren Sie Ihren Problemen den Rücken</p>
</section>

<section class="card card-back" aria-label="Rückseite">
  <svg class="card-art" viewBox="0 0 1302 788" preserveAspectRatio="none" aria-hidden="true">
    <defs>
      <linearGradient id="panel" x1="0" y1="0" x2=".6" y2="1">
        <stop offset="0" stop-color="var(--teal)"/>
        <stop offset="1" stop-color="var(--petrol)"/>
      </linearGradient>
      <linearGradient id="edge" x1="0" y1="0" x2="1" y2="0">
        <stop offset="0" stop-color="var(--petrol-deep)"/>
        <stop offset="1" stop-color="var(--teal)" stop-opacity=".9"/>
      </linearGradient>
    </defs>
    <polygon points="0,0 492,0 465,220 520,470 720,788 0,788" fill="url(#edge)"/>
    <polygon points="0,0 365,0 380,250 470,520 680,788 0,788" fill="url(#panel)"/>
  </svg>

  <h2 class="brand brand-back">
    <span class="brand-kicker">CHIROPRAXIS</span>
    <span class="brand-name">VERTA</span>
  </h2>

  <p class="holder">
    <span class="holder-name">JANATHAN DOE</span>
    <span class="holder-role">Job Tittle Here</span>
  </p>

  <ul class="contact-list">
    <li class="contact-item">
      <svg class="contact-icon" viewBox="0 0 28 28" aria-hidden="true"><circle cx="14" cy="14" r="14" fill="var(--teal)"/><path d="M7 14 L14 8 L21 14 M9 13 V20 H19 V13" fill="none" stroke="var(--white)" stroke-width="2"/><rect x="12.5" y="15.5" width="3" height="4.5" fill="var(--white)"/></svg>
      <span>CITY ADDRESS,STREET<br>HOME LOCATION GOES HERE</span>
    </li>
    <li class="contact-item">
      <svg class="contact-icon" viewBox="0 0 28 28" aria-hidden="true"><circle cx="14" cy="14" r="14" fill="var(--teal)"/><path d="M7 9 L21 14 L7 19 L10 14 Z" fill="var(--white)"/></svg>
      <span>BRAND-NAME@EMAIL.COM</span>
    </li>
    <li class="contact-item">
      <svg class="contact-icon" viewBox="0 0 28 28" aria-hidden="true"><circle cx="14" cy="14" r="14" fill="var(--teal)"/><path d="M7 12 C10 8 18 8 21 12 L19 14 L17 12 H11 L9 14 Z" fill="var(--white)"/><rect x="8" y="15" width="12" height="5" rx="1" fill="var(--white)"/></svg>
      <span class="contact-phone">+000 1234 5678 999<br>+012 9934 5271 003</span>
    </li>
  </ul>
</section>

</body>
</html>
```